Halvern Power "Unique Process" Graphic

Create a "graphic" that creatively represents the seven-step process that Halvern Power uses to serve our customers.
This graphic should be sized in such a way that it can easily be included on a page in our website, and also used in other marketing materials such as flyers, emails and powerpoint presentations.
As an EXAMPLE of a similar graphic, see the "Proven Process" section of the home page of this website - https://www.trelvonsite.com/
I'll include our brand documentation as well as the document for our "Unique Process" in the uploaded files section.
Please use our brand colors and also be creative in how you represent the seven steps graphically.
Here's a bit about our business.
Halvern Power is one of the largest B2B Energy Brokers in the US. We serve tens of thousands of customers by securing energy contracts for them. We are NOT an energy company ourselves - but a broker that represents 30+ energy suppliers to commercial and nonprofit customers.

```html
<!DOCTYPE html>
<html lang="en">
<head>
<meta charset="utf-8">
<title>The Halvern Difference – Seven-Step Process</title>
<link href="https://fonts.googleapis.com/css2?family=Lato:wght@300;400;700;900&display=swap" rel="stylesheet">
<style>
  :root {
    --step-1: #9dd4ab;
    --step-2: #62bf86;
    --step-3: #17ab5c;
    --step-4: #00994c;
    --step-5: #6c7ba8;
    --step-6: #35528b;
    --step-7: #1b3465;
    --green-text: #19a85a;
    --qa-text: #3a5f4d;
    --monitor-text: #6c7ba8;
    --renew-text: #35528b;
    --guarantee-text: #2b3a5e;
    --brand-navy: #1b3465;
    --body-text: #555a5e;
    --rule: #b9bcbf;
    --paper: #ffffff;
  }
  * { margin: 0; padding: 0; box-sizing: border-box; }
  html, body { width: 1200px; height: 675px; overflow: hidden; background: var(--paper); }
  body { font-family: "Lato", Arial, sans-serif; color: var(--body-text); }
  .canvas { position: relative; width: 1200px; height: 675px; }
  .process-wheel { position: absolute; left: 0; top: 0; width: 1200px; height: 675px; }

  .step-number {
    position: absolute; font-weight: 300; font-size: 23px; line-height: 1; letter-spacing: 0.5px;
  }
  .step-rule { position: absolute; height: 1px; background: var(--rule); }
  .step-title {
    position: absolute; white-space: nowrap; font-size: 16.5px; line-height: 1; font-weight: 400;
    letter-spacing: 0.2px;
  }
  .step-title strong { font-weight: 900; }
  .step-body { position: absolute; font-size: 10.6px; line-height: 15px; font-weight: 400; white-space: nowrap; }
  .step-body span { display: block; }
  .step-body strong { font-weight: 700; color: #33383c; }
  .align-right { text-align: right; }

  .tone-green { color: var(--green-text); }
  .tone-qa { color: var(--qa-text); }
  .tone-monitor { color: var(--monitor-text); }
  .tone-renew { color: var(--renew-text); }
  .tone-guarantee { color: var(--guarantee-text); }

  .brand-name {
    position: absolute; left: 100px; top: 548px; color: var(--brand-navy);
    font-weight: 700; font-size: 22px; line-height: 1; white-space: nowrap;
  }
</style>
</head>
<body>
<div class="canvas">

  <svg class="process-wheel" viewBox="0 0 1200 675" aria-hidden="true">
    <g class="wheel-segments" stroke="#fff" stroke-width="3">
      <path fill="var(--step-1)" d="M436 352 A169 169 0 0 1 485.5 232.5 L535 282 A99 99 0 0 0 506 352 Z"/>
      <path fill="var(--step-2)" d="M485.5 232.5 A169 169 0 0 1 605 183 L605 253 A99 99 0 0 0 535 282 Z"/>
      <path fill="var(--step-3)" d="M605 183 A169 169 0 0 1 724.5 232.5 L675 282 A99 99 0 0 0 605 253 Z"/>
      <path fill="var(--step-4)" d="M724.5 232.5 A169 169 0 0 1 774 352 L704 352 A99 99 0 0 0 675 282 Z"/>
      <path fill="var(--step-5)" d="M774 352 A169 169 0 0 1 724.5 471.5 L675 422 A99 99 0 0 0 704 352 Z"/>
      <path fill="var(--step-6)" d="M724.5 471.5 A169 169 0 0 1 605 521 L605 451 A99 99 0 0 0 675 422 Z"/>
      <path fill="var(--step-7)" d="M605 521 A169 169 0 0 1 485.5 471.5 L535 422 A99 99 0 0 0 605 451 Z"/>
    </g>

    <g class="inner-track" fill="none" stroke-width="4" stroke-linecap="round" stroke-dasharray="55 429">
      <circle cx="605" cy="352" r="77" stroke="var(--step-1)" transform="rotate(182 605 352)"/>
      <circle cx="605" cy="352" r="77" stroke="var(--step-2)" transform="rotate(227 605 352)"/>
      <circle cx="605" cy="352" r="77" stroke="var(--step-3)" transform="rotate(272 605 352)"/>
      <circle cx="605" cy="352" r="77" stroke="var(--step-4)" transform="rotate(317 605 352)"/>
      <circle cx="605" cy="352" r="77" stroke="var(--step-5)" transform="rotate(2 605 352)"/>
      <circle cx="605" cy="352" r="77" stroke="var(--step-6)" transform="rotate(47 605 352)"/>
      <circle cx="605" cy="352" r="77" stroke="var(--step-7)" transform="rotate(92 605 352)"/>
    </g>

    <g class="step-badges" stroke="#fff" stroke-width="3">
      <circle cx="454.4" cy="289.6" r="33" fill="#97d1a7"/>
      <circle cx="542.6" cy="201.4" r="33" fill="#5bb981"/>
      <circle cx="667.4" cy="201.4" r="33" fill="var(--step-3)"/>
      <circle cx="755.6" cy="289.6" r="33" fill="var(--step-4)"/>
      <circle cx="755.6" cy="414.4" r="33" fill="var(--step-5)"/>
      <circle cx="667.4" cy="502.6" r="33" fill="var(--step-6)"/>
      <circle cx="542.6" cy="502.6" r="33" fill="var(--step-7)"/>
    </g>

    <g class="badge-icons" fill="#fff">
      <!-- document -->
      <path d="M444 275 h15 l6 6 v21 a2 2 0 0 1 -2 2 h-19 a2 2 0 0 1 -2 -2 v-25 a2 2 0 0 1 2 -2 z"/>
      <g stroke="#97d1a7" stroke-width="1.6"><line x1="447" y1="287" x2="461" y2="287"/><line x1="447" y1="292" x2="461" y2="292"/><line x1="447" y1="297" x2="461" y2="297"/></g>
      <!-- folder -->
      <path d="M529 192 h9 l3 3 h12 a2 2 0 0 1 2 2 v3 h-26 z"/>
      <path d="M528 202 h30 a1.5 1.5 0 0 1 1.5 1.8 l-2.5 9 a2 2 0 0 1 -2 1.4 h-26 a2 2 0 0 1 -2 -2 v-8 a2 2 0 0 1 1 -2.2 z"/>
      <!-- edit -->
      <path d="M656 188 h12 v4 h-8 v18 h18 v-8 h4 v12 h-26 z"/>
      <path d="M677 185 l5 5 -12 12 -6 1 1 -6 z"/>
      <!-- check -->
      <circle cx="755.6" cy="289.6" r="15"/>
      <path d="M748 290 l5 5 10 -10" fill="none" stroke="var(--step-4)" stroke-width="2.6" stroke-linecap="round" stroke-linejoin="round"/>
      <!-- chart board -->
      <rect x="740" y="402" width="31" height="20" rx="2.5"/>
      <path d="M745 417 l6 -6 4 4 9 -9" fill="none" stroke="var(--step-5)" stroke-width="2" stroke-linecap="round" stroke-linejoin="round"/>
      <path d="M755.6 422 l-6 9 M755.6 422 l6 9" stroke="#fff" stroke-width="1.8" stroke-linecap="round"/>
      <!-- hourglass -->
      <path d="M657 486 h21 v4 h-2 q0 8 -7 12.6 q7 4.6 7 12.4 h2 v4 h-21 v-4 h2 q0 -7.8 7 -12.4 q-7 -4.6 -7 -12.6 h-2 z"/>
      <!-- shield -->
      <path d="M542.6 486 l14 5 v8 q0 13 -14 20 q-14 -7 -14 -20 v-8 z"/>
      <path d="M536.5 502 l4.5 5 8 -10" fill="none" stroke="var(--step-7)" stroke-width="2.4" stroke-linecap="round" stroke-linejoin="round"/>
    </g>
  </svg>

  <!-- Step 01 -->
  <section class="step">
    <div class="step-number tone-green" style="left:359px; top:260px;">01</div>
    <div class="step-rule" style="left:192px; width:192px; top:285px;"></div>
    <h2 class="step-title tone-green" style="left:182px; top:293px;"><strong>HALVERN</strong> ASSESSMENT</h2>
    <p class="step-body align-right" style="left:170px; width:222px; top:319px;">
      <span>Spend 15 minutes with our team</span>
      <span>while we analyze your account and</span>
      <span>contract details to select suppliers</span>
      <span style="margin-right:3px;">that fit your needs</span>
    </p>
  </section>

  <!-- Step 02 -->
  <section class="step">
    <div class="step-number tone-green" style="left:479px; top:105px;">02</div>
    <div class="step-rule" style="left:303px; width:201px; top:130px;"></div>
    <h2 class="step-title tone-green" style="left:322px; top:138px;"><strong>HALVERN</strong> OPTIONS!</h2>
    <p class="step-body" style="left:238px; top:163px;">
      <span style="margin-left:26px;">We’ll send you an energy quote with at least 3</span>
      <span style="margin-left:20px;">options to choose from - including different</span>
      <span style="margin-left:7px;">suppliers and contract terms. Our unbiased</span>
      <span>advice will help you find the best solution!</span>
    </p>
  </section>

  <!-- Step 03 -->
  <section class="step">
    <div class="step-number tone-green" style="left:620px; top:50px;">03</div>
    <div class="step-rule" style="left:620px; width:176px; top:76px;"></div>
    <h2 class="step-title tone-green" style="left:629px; top:84px;"><strong>HALVERN</strong> SIGN-UP</h2>
    <p class="step-body" style="left:620px; top:108px;">
      <span>Our simple sign-up process is handled</span>
      <span>electronically. Even contract signatures.</span>
    </p>
  </section>

  <!-- Step 04 -->
  <section class="step">
    <div class="step-number tone-qa" style="left:789px; top:190px;">04</div>
    <div class="step-rule" style="left:794px; width:153px; top:215px;"></div>
    <h2 class="step-title tone-qa" style="left:805px; top:223px;"><strong>HALVERN</strong> QA</h2>
    <p class="step-body" style="left:820px; top:248px;">
      <span>Every order detail is confirmed to ensure</span>
      <span style="margin-left:3px;">accuracy and smooth processing.</span>
    </p>
  </section>

  <!-- Step 05 -->
  <section class="step">
    <div class="step-number tone-monitor" style="left:826px; top:324px;">05</div>
    <div class="step-rule" style="left:826px; width:233px; top:349px;"></div>
    <h2 class="step-title tone-monitor" style="left:834px; top:357px;"><strong>HALVERN</strong> MONITORING</h2>
    <p class="step-body" style="left:824px; top:383px;">
      <span style="margin-left:9px;">We proactively monitor your accounts to</span>
      <span style="margin-left:5px;">address any contractual issues with suppliers,</span>
      <span style="margin-left:2px;">should they arise. (e.g., You sell your business,</span>
      <span>account number changes, etc.)</span>
    </p>
  </section>

  <!-- Step 06 -->
  <section class="step">
    <div class="step-number tone-renew" style="left:759px; top:487px;">06</div>
    <div class="step-rule" style="left:751px; width:232px; top:512px;"></div>
    <h2 class="step-title tone-renew" style="left:752px; top:519px;"><strong>HALVERN</strong> RENEWAL</h2>
    <p class="step-body" style="left:668px; top:545px;">
      <span style="margin-left:54px;">To protect your business from market volatility, we</span>
      <span style="margin-left:36px;">contact you ahead of your contract end date to discuss</span>
      <span style="margin-left:18px;">renewal options. If anyone else contacts you, you respond,</span>
      <span>“No thank you, <strong>we have Halvern</strong>!”</span>
    </p>
  </section>

  <!-- Step 07 -->
  <section class="step">
    <div class="step-number tone-guarantee" style="left:422px; top:540px;">07</div>
    <div class="step-rule" style="left:422px; width:175px; top:565px;"></div>
    <h2 class="step-title tone-guarantee" style="left:431px; top:573px;"><strong>HALVERN</strong> GUARANTEE</h2>
    <p class="step-body" style="left:422px; top:599px;">
      <span>Sleep Easy! You’ll never fall “out of</span>
      <span>contract” with <strong>Halvern</strong> as your broker.</span>
    </p>
  </section>

  <div class="brand-name">The Halvern Difference</div>

</div>
</body>
</html>
```